Flyer Design Project

We want to design a flyer for a laundromat in San Francisco. It will be used to market the services of the laundromat. I am uploading a .jpg file with details to be highlighted. The flyer should be of size 8.5 in x 11 in and should be attractive and hard hitting. The attachment should only be used for the copy, not for design.

Target Market(s)

Laundromat and laundry users

Requirements
Must have
• Must have a attention grabbing headline
Nice to have
• Pictures

```html
<!DOCTYPE html>
<html lang="en">
<head>
<meta charset="utf-8">
<title>Marlowe Laundromat Flyer</title>
<link rel="stylesheet" href="https://fonts.googleapis.com/css2?family=Arimo:wght@400;700&family=PT+Sans+Narrow:wght@700&family=Sniglet:wght@800&display=swap">
<style>
  :root {
    --sky-light: #6fb2ea;
    --sky-mid: #4b95dc;
    --sky-deep: #2f78c9;
    --navy: #1f1f86;
    --navy-deep: #15156a;
    --leaf: #1f9a3a;
    --leaf-dark: #137a2a;
    --lime: #8fcf3c;
    --headline-fill: #c9e84a;
    --headline-edge: #1a2a10;
    --frame: #e9eef0;
    --frame-shade: #a9b4b8;
    --white: #ffffff;
    --photo-warm: #c9a58e;
    --photo-cool: #9aa3ad;
  }
  * { box-sizing: border-box; margin: 0; padding: 0; }
  html, body { width: 950px; height: 1200px; overflow: hidden; background: #eeeeee; }
  .flyer {
    position: relative;
    width: 950px; height: 1200px;
    overflow: hidden;
    background: radial-gradient(ellipse at 35% 40%, var(--sky-light) 0%, var(--sky-mid) 55%, var(--sky-deep) 100%);
    font-family: "Arimo", Arial, sans-serif;
  }
  .swoosh { position: absolute; inset: 0; width: 950px; height: 1200px; }

  .brand { position: absolute; left: 36px; top: 32px; display: flex; align-items: center; gap: 18px; }
  .brand-mark { width: 112px; height: 112px; border-radius: 50%; background: var(--frame); border: 6px solid var(--frame-shade); }
  .brand-name { color: var(--white); font-family: "Arimo", Arial, sans-serif; font-weight: 400; font-size: 42px; line-height: 56px; letter-spacing: -0.5px; }

  .headline {
    position: absolute; left: 44px; top: 256px; width: 556px;
    white-space: nowrap;
    font-family: "Sniglet", "Comic Sans MS", cursive;
    font-weight: 800; font-size: 28px; line-height: 40px;
    color: var(--headline-fill);
    -webkit-text-stroke: 1.2px var(--headline-edge);
    text-shadow: 2px 2px 0 var(--headline-edge);
  }

  .card { position: absolute; width: 268px; height: 264px; }
  .card svg { position: absolute; inset: 0; width: 100%; height: 100%; }
  .card-text { position: absolute; left: 22px; right: 26px; top: 0; bottom: 18px; display: flex; flex-direction: column; justify-content: center; color: var(--white); }
  .card-title { font-family: "PT Sans Narrow", "Arial Narrow", sans-serif; font-weight: 700; font-size: 27px; line-height: 33px; text-transform: uppercase; margin-bottom: 14px; padding-right: 40px; }
  .card-body { font-size: 16.5px; line-height: 22px; text-align: center; }

  .card--parking { left: 36px; top: 318px; }
  .card--washers { left: 336px; top: 436px; }
  .card--dropoff { left: 632px; top: 21px; }
  .card--grocery { left: 632px; top: 316px; }
  .card--leisure { left: 632px; top: 620px; }

  .interior-photo {
    position: absolute; left: 21px; top: 815px; width: 650px; height: 372px;
    border-radius: 50%;
    background: linear-gradient(180deg, #e4e2dc 0%, var(--photo-cool) 55%, #5f6870 100%);
    box-shadow: 10px 0 0 6px #1d5fb8;
  }
  .customer-photo {
    position: absolute; left: 18px; top: 594px; width: 312px; height: 606px;
    border-radius: 120px 120px 30px 30px;
    background: linear-gradient(180deg, var(--photo-warm) 0%, #d877a6 30%, #4f7fb3 55%, #3a5680 100%);
  }

  .contact { position: absolute; right: 24px; top: 1120px; text-align: right; color: var(--white); }
  .contact-phone { font-family: "PT Sans Narrow", "Arial Narrow", sans-serif; font-weight: 700; font-size: 33px; line-height: 40px; }
  .contact-web { font-size: 16.5px; line-height: 24px; }
  .footer-mark { position: absolute; left: 784px; top: 990px; width: 110px; height: 110px; border-radius: 50%; background: var(--frame); border: 6px solid var(--frame-shade); }
</style>
</head>
<body>
<main class="flyer">
  <svg class="swoosh" viewBox="0 0 950 1200" aria-hidden="true">
    <path d="M0 160 C70 205 170 225 270 205 C420 175 520 90 611 0" fill="none" stroke="var(--lime)" stroke-width="12"/>
    <path d="M0 0 H611 C530 70 420 160 260 192 C160 212 60 190 0 150 Z" fill="var(--navy)"/>
    <path d="M430 1200 C580 1110 760 1060 950 1035" fill="none" stroke="var(--lime)" stroke-width="12"/>
    <path d="M470 1200 C620 1125 790 1075 950 1058 V1200 Z" fill="var(--navy)"/>
  </svg>

  <div class="brand">
    <div class="brand-mark"></div>
    <div class="brand-name">marlowe<br>laundromat</div>
  </div>

  <h1 class="headline">Fast Forward Your Laundry Day!</h1>

  <div class="interior-photo" role="img" aria-label="Photo of the laundromat interior with rows of commercial washers and dryers"></div>
  <div class="customer-photo" role="img" aria-label="Photo of a smiling customer holding a basket of laundry"></div>

  <section class="card card--parking">
    <svg viewBox="0 0 268 262" preserveAspectRatio="none" aria-hidden="true">
      <path d="M28 2 H180 L265 150 V232 Q265 260 237 260 H28 Q2 260 2 232 V30 Q2 2 28 2 Z" fill="var(--frame)" stroke="var(--leaf)" stroke-width="3"/>
      <path d="M36 16 H172 L250 156 V224 Q250 244 230 244 H36 Q16 244 16 224 V36 Q16 16 36 16 Z" fill="var(--leaf)"/>
      <path d="M180 2 C200 50 225 100 265 150 C225 130 195 90 168 30 Z" fill="var(--frame-shade)"/>
      <path d="M182 10 C198 50 214 80 236 108 L250 156 C215 120 195 80 182 10 Z" fill="var(--leaf-dark)"/>
    </svg>
    <div class="card-text">
      <h2 class="card-title">Have large<br>laundry loads?</h2>
      <p class="card-body">bring them in your car:<br>we have ample parking</p>
    </div>
  </section>

  <section class="card card--washers">
    <svg viewBox="0 0 268 262" preserveAspectRatio="none" aria-hidden="true">
      <path d="M28 2 H180 L265 150 V232 Q265 260 237 260 H28 Q2 260 2 232 V30 Q2 2 28 2 Z" fill="var(--frame)" stroke="var(--leaf)" stroke-width="3"/>
      <path d="M36 16 H172 L250 156 V224 Q250 244 230 244 H36 Q16 244 16 224 V36 Q16 16 36 16 Z" fill="var(--leaf)"/>
      <path d="M180 2 C200 50 225 100 265 150 C225 130 195 90 168 30 Z" fill="var(--frame-shade)"/>
      <path d="M182 10 C198 50 214 80 236 108 L250 156 C215 120 195 80 182 10 Z" fill="var(--leaf-dark)"/>
    </svg>
    <div class="card-text">
      <h2 class="card-title">Hate doing<br>laundry?</h2>
      <p class="card-body">we will fast forward your<br>day with our large<br>commercial washers<br>and dryers: you will be<br>out of here in no time</p>
    </div>
  </section>

  <section class="card card--dropoff">
    <svg viewBox="0 0 268 262" preserveAspectRatio="none" aria-hidden="true">
      <path d="M28 2 H180 L265 150 V232 Q265 260 237 260 H28 Q2 260 2 232 V30 Q2 2 28 2 Z" fill="var(--frame)" stroke="var(--leaf)" stroke-width="3"/>
      <path d="M36 16 H172 L250 156 V224 Q250 244 230 244 H36 Q16 244 16 224 V36 Q16 16 36 16 Z" fill="var(--leaf)"/>
      <path d="M180 2 C200 50 225 100 265 150 C225 130 195 90 168 30 Z" fill="var(--frame-shade)"/>
      <path d="M182 10 C198 50 214 80 236 108 L250 156 C215 120 195 80 182 10 Z" fill="var(--leaf-dark)"/>
    </svg>
    <div class="card-text">
      <h2 class="card-title">No time<br>for laundry?</h2>
      <p class="card-body">bring it to us and<br>collect it washed, folded<br>and neatly packed<br>after 24 hours</p>
    </div>
  </section>

  <section class="card card--grocery">
    <svg viewBox="0 0 268 262" preserveAspectRatio="none" aria-hidden="true">
      <path d="M28 2 H180 L265 150 V232 Q265 260 237 260 H28 Q2 260 2 232 V30 Q2 2 28 2 Z" fill="var(--frame)" stroke="var(--leaf)" stroke-width="3"/>
      <path d="M36 16 H172 L250 156 V224 Q250 244 230 244 H36 Q16 244 16 224 V36 Q16 16 36 16 Z" fill="var(--leaf)"/>
      <path d="M180 2 C200 50 225 100 265 150 C225 130 195 90 168 30 Z" fill="var(--frame-shade)"/>
      <path d="M182 10 C198 50 214 80 236 108 L250 156 C215 120 195 80 182 10 Z" fill="var(--leaf-dark)"/>
    </svg>
    <div class="card-text">
      <h2 class="card-title">No time for<br>grocery<br>shopping?</h2>
      <p class="card-body">do your grocery shopping<br>at nearby greenleaf market<br>while our machines do<br>your laundry</p>
    </div>
  </section>

  <section class="card card--leisure">
    <svg viewBox="0 0 268 262" preserveAspectRatio="none" aria-hidden="true">
      <path d="M28 2 H180 L265 150 V232 Q265 260 237 260 H28 Q2 260 2 232 V30 Q2 2 28 2 Z" fill="var(--frame)" stroke="var(--leaf)" stroke-width="3"/>
      <path d="M36 16 H172 L250 156 V224 Q250 244 230 244 H36 Q16 244 16 224 V36 Q16 16 36 16 Z" fill="var(--leaf)"/>
      <path d="M180 2 C200 50 225 100 265 150 C225 130 195 90 168 30 Z" fill="var(--frame-shade)"/>
      <path d="M182 10 C198 50 214 80 236 108 L250 156 C215 120 195 80 182 10 Z" fill="var(--leaf-dark)"/>
    </svg>
    <div class="card-text">
      <h2 class="card-title">Get bored<br>doing<br>laundry?</h2>
      <p class="card-body">not here! we have<br>free wi fi and flat screen<br>tv to keep<br>you entertained</p>
    </div>
  </section>

  <div class="footer-mark"></div>
  <footer class="contact">
    <p class="contact-phone">Ph: (415) 555-0172</p>
    <p class="contact-web">www.marlowelaundromat.com</p>
  </footer>
</main>
</body>
</html>
```